Managed IT services business card design

We haven't needed a business card since the founding of the business in 2005. All our clients have been coming through word of mouth. And lately more and more existing clients are requesting for our business cards to pass on to their contacts in recommending us.
So we needing a business card design. We use various innovative solutions and methodologies to provide IT services to small businesses in managing their IT systems. Our role is the same as an in-house, full-time IT Manager for our clients, but outsourced. So we take care of all our clients' IT needs, just as an IT Manager would be expected to perform.
We have a holding website, which we're happy to leave for now. If we can use the same logo would be great - www.tegvu.com.au
Preferred colours are shades of are white, grey and black.
We pride our business with the following traits: proactive, good service, prompt response, trustworthy.
Target Market(s)
Small businesses of any industry
Industry/Entity Type
Business

```html
<!DOCTYPE html>
<html lang="en">
<head>
<meta charset="utf-8">
<title>tegvu business card</title>
<link rel="stylesheet" href="https://fonts.googleapis.com/css2?family=Open+Sans:wght@400;700&display=swap">
<style>
  :root {
    --backdrop-top: #9ea3ad;
    --backdrop-bottom: #c9ccd2;
    --card-white: #f7f7f7;
    --card-shade: #dcdcdc;
    --panel-dark: #3a3a3c;
    --swoosh-grey: #a7a7a9;
    --ink-dark: #2e2e30;
    --ink-light: #ffffff;
  }
  * { box-sizing: border-box; margin: 0; padding: 0; }
  html, body { width: 1200px; height: 866px; overflow: hidden; }
  body {
    background: linear-gradient(160deg, var(--backdrop-top), var(--backdrop-bottom));
    font-family: "Open Sans", Arial, sans-serif;
    position: relative;
  }
  .card {
    position: absolute;
    width: 560px;
    height: 320px;
    background: radial-gradient(circle at 55% 50%, var(--card-white), var(--card-shade));
    box-shadow: 0 10px 30px rgba(0,0,0,0.25);
    overflow: hidden;
  }
  .card--front { left: 110px; top: 90px; }
  .card--back { left: 530px; top: 456px; }

  .brand-name {
    position: absolute;
    color: var(--ink-dark);
    font-weight: 400;
    letter-spacing: normal;
    line-height: 1;
    white-space: nowrap;
  }
  .card--front .brand-name { left: 50%; top: 50%; transform: translate(-50%, -50%); font-size: 42px; }
  .card--back .brand-name { left: 50px; top: 138px; font-size: 32px; }

  .back-art { position: absolute; inset: 0; width: 100%; height: 100%; }

  .contact {
    position: absolute;
    right: 24px;
    top: 22px;
    text-align: right;
    color: var(--ink-light);
    font-size: 13px;
    line-height: 1.35;
  }
  .contact__name { font-weight: 700; font-size: 15px; }
  .contact__role { margin-bottom: 34px; }
  .contact__address { margin-bottom: 16px; }
  .contact__line { display: flex; justify-content: flex-end; align-items: center; gap: 6px; }
  .contact__icon { width: 11px; height: 11px; fill: var(--ink-light); }
</style>
</head>
<body>

  <section class="card card--front">
    <p class="brand-name">tegvu</p>
  </section>

  <section class="card card--back">
    <svg class="back-art" viewBox="0 0 560 320" preserveAspectRatio="none" aria-hidden="true">
      <path d="M200,0 C330,45 360,200 318,320 L560,320 L560,0 Z" fill="var(--panel-dark)"/>
      <path d="M214,0 C332,52 356,200 326,320 L346,320 C378,200 350,48 236,0 Z" fill="var(--swoosh-grey)"/>
      <path d="M230,0 C340,50 366,200 340,320" stroke="var(--card-white)" stroke-width="3" fill="none"/>
    </svg>

    <p class="brand-name">tegvu</p>

    <div class="contact">
      <p class="contact__name">Marlen Ostby-Crane</p>
      <p class="contact__role">Consultant</p>
      <p class="contact__address">42 Level 9, Arden House<br>Harbour Street NSW</p>
      <p class="contact__line">02 5550 1470
        <svg class="contact__icon" viewBox="0 0 24 24"><path d="M6.6 10.8a15 15 0 0 0 6.6 6.6l2.2-2.2a1 1 0 0 1 1-.25 11 11 0 0 0 3.6.6 1 1 0 0 1 1 1V20a1 1 0 0 1-1 1A17 17 0 0 1 3 4a1 1 0 0 1 1-1h3.5a1 1 0 0 1 1 1 11 11 0 0 0 .6 3.6 1 1 0 0 1-.25 1z"/></svg>
      </p>
      <p class="contact__line">02 5550 1471
        <svg class="contact__icon" viewBox="0 0 24 24"><path d="M6 2h9l3 3v5H6zM3 11h18v10H3zm4 3v2h3v-2zm0 3v2h3v-2zm5-3v2h3v-2zm0 3v2h3v-2z"/></svg>
      </p>
      <p class="contact__line">hello@tegvu.com.au
        <svg class="contact__icon" viewBox="0 0 24 24"><path d="M2 5h20v14H2zm2 2v.5l8 5 8-5V7z"/></svg>
      </p>
      <p class="contact__line">www.tegvu.com.au</p>
    </div>
  </section>

</body>
</html>
```